Coffee Shop needs a fresh new menu

Hi,
I would like a new menu to be designed for our coffee shop.
We display our menu on a television screen, so would need it in a file that would allow us to continue to do so -- I have attached a photo so that you can see our current design, and how it is displayed.

I'd like something that is easy to read, if the design could have a "hipster" feel to it -- we are located at a hospital and University.

I have attached a Word file with what we would like on the menu.

Feel free to contact me if you have any questions.

Thanks,
Tam

Just A4 size will be fine, and no need to include menu 1 and menu 2 - I just put them in as an example of what we already have -- they are our printed menu's. Thanks

Hospital

```html
<!DOCTYPE html>
<html lang="en">
<head>
<meta charset="utf-8">
<title>Rounds Canteen Menu</title>
<link href="https://fonts.googleapis.com/css2?family=PT+Sans:wght@400;700&family=PT+Sans+Narrow:wght@400;700&display=swap" rel="stylesheet">
<style>
  :root {
    --red: #e21a37;
    --red-deep: #c8102e;
    --charcoal: #3b3b3d;
    --ink: #222;
    --paper-top: #f6f6f6;
    --paper-bottom: #e4e4e6;
    --rule: #9a9a9a;
    --backdrop: #ffffff;
    --tone-coffee-a: #efe6d8;
    --tone-coffee-b: #c99562;
    --tone-bread-a: #e3a24a;
    --tone-bread-b: #b9652a;
    --tone-burger-a: #d99043;
    --tone-burger-b: #8a5a2e;
    --tone-salad-a: #e9eedf;
    --tone-salad-b: #86b457;
    --tone-wrap-a: #f2e8d4;
    --tone-wrap-b: #d4b07e;
  }
  * { box-sizing: border-box; margin: 0; padding: 0; }
  html, body { width: 925px; height: 1200px; overflow: hidden; background: var(--backdrop); }
  body { font-family: "PT Sans", sans-serif; color: var(--ink); }

  .menu {
    position: absolute; left: 36px; top: 0; width: 853px; height: 1200px;
    background: linear-gradient(180deg, var(--paper-top), var(--paper-bottom));
    overflow: hidden;
  }

  .brand { position: absolute; left: 80px; top: 96px; display: flex; align-items: center; gap: 16px; }
  .brand-dot { width: 64px; height: 64px; border-radius: 50%; background: var(--red); }
  .brand-name { font-weight: 700; font-size: 54px; color: var(--red); letter-spacing: 1px; }

  .intro {
    position: absolute; left: 400px; top: 44px; width: 400px;
    text-align: center; color: var(--red); font-weight: 700; font-size: 27px; line-height: 34px;
  }

  .tab { position: absolute; background: var(--charcoal); }
  .tab-top { left: 400px; top: 237px; width: 453px; height: 40px; border-top-left-radius: 26px; }
  .tab-bottom { left: 0; top: 766px; width: 405px; height: 38px; border-radius: 0 24px 24px 0; }

  .band { position: absolute; left: 0; top: 275px; width: 853px; height: 466px; background: linear-gradient(180deg, var(--red), var(--red-deep)); }

  .coffee-card {
    position: absolute; left: 38px; top: 295px; width: 400px; height: 440px;
    background: linear-gradient(180deg, #fff, #ededed); border-radius: 14px;
    box-shadow: 0 4px 10px rgba(0,0,0,.35);
  }
  .section-title { position: absolute; font-weight: 700; line-height: 1; }
  .coffee-title { left: 25px; top: 16px; font-family: "PT Sans Narrow", sans-serif; font-size: 31px; color: var(--red); }

  .rows { position: absolute; list-style: none; font-size: 15px; line-height: 20.4px; }
  .rows li { display: flex; }
  .coffee-rows .name { width: 117px; }
  .coffee-rows .small { width: 116px; }
  .espresso-rows .name { width: 138px; }
  .rule { position: absolute; left: 20px; width: 340px; height: 1px; background: var(--rule); }
  .extras { position: absolute; left: 25px; top: 372px; font-size: 15px; line-height: 20.4px; }

  .photo { position: absolute; border-radius: 18px; }
  .photo-cup { left: 305px; top: 600px; width: 190px; height: 135px; background: linear-gradient(160deg, var(--tone-coffee-a), var(--tone-coffee-b)); }
  .photo-croissant { left: 590px; top: 582px; width: 230px; height: 140px; background: linear-gradient(180deg, var(--tone-bread-a), var(--tone-bread-b)); }
  .photo-burger { left: 600px; top: 806px; width: 220px; height: 170px; background: linear-gradient(180deg, var(--tone-burger-a), var(--tone-burger-b)); }
  .photo-salad { left: 590px; top: 990px; width: 230px; height: 150px; background: linear-gradient(180deg, var(--tone-salad-a), var(--tone-salad-b)); }
  .photo-wrap { left: 345px; top: 1078px; width: 170px; height: 108px; background: linear-gradient(150deg, var(--tone-wrap-a), var(--tone-wrap-b)); }

  .breakfast-title { left: 457px; top: 300px; font-size: 31px; color: #fff; }
  .breakfast-rows { left: 462px; top: 356px; color: #fff; line-height: 23.5px; }
  .breakfast-rows .name { width: 238px; }

  .lower-title { top: 820px; font-size: 24px; color: var(--red); }
  .lower-rule { position: absolute; top: 860px; height: 1px; background: var(--rule); }
  .lower-rows { top: 866px; line-height: 23.5px; }
  .hot-rows .name { width: 204px; }
  .light-rows .name { width: 131px; }
</style>
</head>
<body>
<main class="menu">
  <div class="brand">
    <span class="brand-dot"></span>
    <span class="brand-name">ROUNDS</span>
  </div>

  <p class="intro">Our Store inside the Hospital Food Court sells: Hot Pies, Assorted Pasta’s, Ready -to-go Meals, Quiche, and lots more!</p>

  <div class="tab tab-top"></div>
  <div class="band"></div>
  <div class="tab tab-bottom"></div>

  <section class="coffee-card">
    <h2 class="section-title coffee-title">COFFEE:</h2>
    <ul class="rows coffee-rows" style="left:25px;top:58px">
      <li><span class="name">Latte</span><span class="small">small $4.0</span><span>Large $4.50</span></li>
      <li><span class="name">Cappuccino</span><span class="small">small $4.0</span><span>Large $4.50</span></li>
      <li><span class="name">Flat White</span><span class="small">small $4.0</span><span>Large $4.50</span></li>
      <li><span class="name">Long Black</span><span class="small">small $4.0</span><span>Large $4.50</span></li>
      <li><span class="name">Hot Chocolate</span><span class="small">small $4.0</span><span>Large $4.50</span></li>
    </ul>
    <div class="rule" style="top:163px"></div>
    <ul class="rows coffee-rows" style="left:25px;top:180px">
      <li><span class="name">Chai Latte</span><span class="small">small $4.50</span><span>Large $5.0</span></li>
      <li><span class="name">Mocha</span><span class="small">small $4.50</span><span>Large $5.0</span></li>
      <li><span class="name">Dirty Chai</span><span class="small">small &nbsp;$5</span><span>Large $5.50</span></li>
    </ul>
    <div class="rule" style="top:246px"></div>
    <ul class="rows espresso-rows" style="left:25px;top:263px">
      <li><span class="name">Espresso</span><span>$3.50</span></li>
      <li><span class="name">Short Macchiato</span><span>$4.0</span></li>
      <li><span class="name">Piccolo</span><span>$4.0</span></li>
      <li><span class="name">Long Macchiato</span><span>$4.50</span></li>
    </ul>
    <p class="extras">Extras<br>Soy Milk/Lactose Free Milk/Syrups/<br>Extra Shot/Decaf &nbsp;$0.50 extra</p>
  </section>
  <div class="photo photo-cup" role="img" aria-label="Photo of a cup of cappuccino on a saucer"></div>

  <h2 class="section-title breakfast-title">Breakfast Items</h2>
  <ul class="rows breakfast-rows">
    <li><span class="name">Bacon, Egg and Cheese Roll</span><span>$6.0</span></li>
    <li><span class="name">Ham and Cheese Toastie</span><span>$5.0</span></li>
    <li><span class="name">Cheese and Tomato Toastie</span><span>$5.0</span></li>
    <li><span class="name">Ham and Cheese Croissant</span><span>$6.0</span></li>
    <li><span class="name">Cheese and Tomato Croissant</span><span>$5.50</span></li>
    <li><span class="name">Plain Croissant</span><span>$3.50</span></li>
    <li><span class="name">Hash Brown</span><span>$2.0</span></li>
    <li><span class="name">2 Piece Toast</span><span>$3.0</span></li>
    <li><span class="name">2 Piece Rasin Toast</span><span>$3.0</span></li>
  </ul>
  <div class="photo photo-croissant" role="img" aria-label="Photo of a croissant sandwich with bacon, egg and cheese"></div>

  <h2 class="section-title lower-title" style="left:44px">Hot Food and Sandwiches</h2>
  <div class="lower-rule" style="left:44px;width:302px"></div>
  <ul class="rows lower-rows hot-rows" style="left:44px">
    <li><span class="name">Pre Made Sandwiches</span><span>$6.50 - $7.50</span></li>
    <li><span class="name">Pre Made Focaccias</span><span>$8.50</span></li>
    <li><span class="name">Wraps</span><span>$7.50</span></li>
    <li><span class="name">Vegetarian Salad</span><span>$7.50</span></li>
    <li><span class="name">Meat/Seafood Salad</span><span>$9.50</span></li>
    <li><span class="name">Hot Chips</span><span>$4.50</span></li>
    <li><span class="name">Dim Sim</span><span>$1.50</span></li>
    <li><span class="name">Potato Cake</span><span>$1.50</span></li>
    <li><span class="name">Plain Hamburger</span><span>$7.50</span></li>
    <li><span class="name">Hamburger with the lot</span><span>$9.0</span></li>
    <li><span class="name">Chicken Schnitzel Burger</span><span>$8.50</span></li>
  </ul>

  <h2 class="section-title lower-title" style="left:378px">Something Light</h2>
  <div class="lower-rule" style="left:378px;width:190px"></div>
  <ul class="rows lower-rows light-rows" style="left:378px;top:870px">
    <li><span class="name">Mixed Yoghurts</span><span>$5.50</span></li>
    <li><span class="name">Chia Pudding</span><span>$5.50</span></li>
    <li><span class="name">Fruit Salad</span><span>$5.50</span></li>
    <li><span class="name">Bircher Muesli</span><span>$5.50</span></li>
    <li><span class="name">Protein Balls</span><span>$4.0</span></li>
    <li><span class="name">Banana Bread</span><span>$4.50</span></li>
    <li><span class="name">Muffins</span><span>$4.50</span></li>
    <li><span class="name">Slices</span><span>$4.0</span></li>
  </ul>

  <div class="photo photo-burger" role="img" aria-label="Photo of a hamburger with lettuce, tomato and cheese"></div>
  <div class="photo photo-salad" role="img" aria-label="Photo of a chicken salad in a white bowl"></div>
  <div class="photo photo-wrap" role="img" aria-label="Photo of a chicken and salad wrap"></div>
</main>
</body>
</html>
```